Company Mission & Values Poster

I'd like an A2 Portrait Poster displaying our company's Mission & Values.
See our website for our logo, fonts, mission & values.
https://talvendo.com.au/

Our Mission: Creating homes for abundant life
Values: Love, Thinking, Team, Zoe.

Some ideas to consider:
Mission as the Headline then
A logo for each of the 4 Values and the words

Target Market(s)

Myself & my team

Industry/Entity Type

Real Estate

Font styles to use
Other font styles liked:
• Company fonts as seen on our website

```html
<!DOCTYPE html>
<html lang="en">
<head>
<meta charset="utf-8">
<title>Talvendo – Mission &amp; Values Poster</title>
<link rel="stylesheet" href="https://fonts.googleapis.com/css2?family=Gelasio:wght@400;500&family=Poppins:wght@300;400&display=swap">
<style>
  :root {
    --ink: #0b3a33;
    --ink-soft: #5f7f78;
    --tint: #dfe7e4;
    --paper: #f7f7f5;
    --stage: #e8e6e2;
    --line: #8a8f8c;
    --body-text: #1d2a27;
    --reverse: #ffffff;
  }
  * { box-sizing: border-box; margin: 0; padding: 0; }
  html, body {
    width: 1200px; height: 1200px; overflow: hidden;
    background: var(--stage);
  }
  .poster {
    position: absolute; left: 191px; top: 20px;
    width: 817px; height: 1160px;
    background: var(--paper);
    overflow: hidden;
    color: var(--ink);
    font-family: "Poppins", sans-serif;
  }
  .poster__art { position: absolute; inset: 0; }
  .wordmark {
    position: absolute; left: 76px; top: 42px;
    font-family: "Gelasio", serif; font-weight: 400;
    font-size: 52px; letter-spacing: 7px; line-height: 1;
    color: var(--ink);
  }
  .section-tag {
    position: absolute; left: 33px; width: 249px; height: 40px;
    background: var(--ink); color: var(--reverse);
    font-size: 17px; font-weight: 300; letter-spacing: 0.5px;
    padding-left: 43px; line-height: 40px;
  }
  .section-tag--mission { top: 114px; }
  .section-tag--values { top: 274px; }
  .mission-title {
    position: absolute; left: 76px; top: 172px;
    font-family: "Gelasio", serif; font-weight: 500;
    font-size: 33px; line-height: 1.1;
  }
  .mission-text {
    position: absolute; left: 76px; top: 210px; width: 600px;
    font-size: 12.8px; line-height: 16.5px; color: var(--body-text);
  }
  .values-title {
    position: absolute; left: 76px; top: 322px; width: 680px;
    font-family: "Gelasio", serif; font-weight: 400;
    font-size: 35.5px; line-height: 35px;
  }
  .value { position: absolute; width: 330px; }
  .value__name {
    font-family: "Gelasio", serif; font-weight: 400;
    font-size: 27px; line-height: 1.1; margin-bottom: 6px;
  }
  .value__text { font-size: 12.6px; line-height: 16.5px; color: var(--body-text); }
  .value--left { left: 344px; }
  .value--right { left: 151px; text-align: right; }
  .value--love { top: 474px; }
  .value--thinking { top: 625px; }
  .value--team { top: 776px; }
  .value--zoe { top: 927px; }
  .value-icon {
    position: absolute; width: 84px; height: 84px;
    border-radius: 14px;
    background: linear-gradient(160deg, var(--tint), #c7d5d1);
  }
  .value-icon--love { left: 161px; top: 492px; }
  .value-icon--thinking { left: 571px; top: 660px; }
  .value-icon--team { left: 161px; top: 800px; }
  .value-icon--zoe { left: 571px; top: 962px; }
  .footer-band {
    position: absolute; left: 0; top: 1092px; width: 100%; height: 45px;
    background: var(--ink); color: var(--reverse);
    font-family: "Gelasio", serif; font-size: 19px; letter-spacing: 1.5px;
    text-align: center; line-height: 45px;
  }
</style>
</head>
<body>
<main class="poster">
  <svg class="poster__art" width="817" height="1160" viewBox="0 0 817 1160" aria-hidden="true">
    <line x1="33" y1="0" x2="33" y2="1092" stroke="var(--ink)" stroke-width="1"/>
    <g fill="none" stroke="var(--line)" stroke-width="1">
      <path d="M76 587 V506 A47 47 0 0 1 123 459 H694 A47 47 0 0 1 741 506 V563 A47 47 0 0 1 694 610
               H123 A47 47 0 0 0 76 657 V714 A47 47 0 0 0 123 761 H184 L204 786 L223 761 H694
               A47 47 0 0 1 741 808 V865 A47 47 0 0 1 694 912 H123 A47 47 0 0 0 76 959 V1016
               A47 47 0 0 0 123 1063 H694 A47 47 0 0 0 741 1016 V935"/>
      <line x1="285" y1="459" x2="285" y2="610"/>
      <path d="M532 610 V670 L508 686 L532 702 V761"/>
      <line x1="285" y1="786" x2="285" y2="912"/>
      <path d="M532 912 V972 L508 988 L532 1004 V1063"/>
    </g>
    <g fill="var(--ink)">
      <circle cx="76" cy="587" r="4.5"/>
      <circle cx="741" cy="935" r="4.5"/>
    </g>
    <g fill="none" stroke="var(--ink)" stroke-width="9">
      <polyline points="288,510 318,535 288,560"/>
      <polyline points="288,814 318,839 288,864"/>
      <polyline points="588,612 613,642 638,612"/>
      <polyline points="588,914 613,944 638,914"/>
    </g>
  </svg>

  <div class="wordmark">TALVENDO</div>

  <div class="section-tag section-tag--mission">OUR MISSION</div>
  <h1 class="mission-title">Creating homes for abundant life.</h1>
  <p class="mission-text">We wholeheartedly believe that home is an extraordinary place: a haven where life unfolds in all its glory. Where we find solace, make cherished memories with loved ones, and savour the natural beauty that surrounds us.</p>

  <div class="section-tag section-tag--values">OUR VALUES</div>
  <h2 class="values-title">We believe business can be a force for good. Our values shape the way we work, and how we make decisions.</h2>

  <div class="value-icon value-icon--love" role="img" aria-label="Icon of arms embracing a heart"></div>
  <section class="value value--left value--love">
    <h3 class="value__name">Love</h3>
    <p class="value__text">Our mission is founded in our love and respect for people - those we develop for, those in our teams and those in the communities we create and operate within.</p>
  </section>

  <div class="value-icon value-icon--thinking" role="img" aria-label="Icon of a brain inside a light bulb"></div>
  <section class="value value--right value--thinking">
    <h3 class="value__name">Thinking</h3>
    <p class="value__text">We believe in the power of thinking. Our rigorous &amp; creative processes create beautifully considered solutions for our purchasers, the communities we develop within and the environment.</p>
  </section>

  <div class="value-icon value-icon--team" role="img" aria-label="Icon of two hands holding a group of people"></div>
  <section class="value value--left value--team">
    <h3 class="value__name">Team</h3>
    <p class="value__text">Property development is a team sport. We surround ourselves with the best designers and advisers. We strive to create an environment that allows them to do their best work and love doing it.</p>
  </section>

  <div class="value-icon value-icon--zoe" role="img" aria-label="Icon of a person celebrating with a tick"></div>
  <section class="value value--right value--zoe">
    <h3 class="value__name">Zoe</h3>
    <p class="value__text">Our mission is to create places for ‘Zoe’ - the Greek word for abundant life. We do this through exquisite design, quality construction and celebrating nature.</p>
  </section>

  <footer class="footer-band">www.talvendo.com.au</footer>
</main>
</body>
</html>
```